KTW accounting firm Canada - Modern and professional business cards

To use our existing logo and create a modern looking business card.
We are looking for double sided style.
Silver-metallic background - our logo in front (reverse side)
The reverse side from the attachment- big logo over silver-metallic background is preferred.
we would like to have a business card template that can be modified to change names, addresses, and other

Industry/Entity Type

Accounting

Contact Information for Business Card

Reverse side silver-metallic finish

Font styles to use
Sans Serif

Requirements
Must have
• Reverse side silver-metallic finish
• Modern look

```html
<!DOCTYPE html>
<html lang="en">
<head>
<meta charset="utf-8">
<title>KTW Business Card – Front and Reverse</title>
<link rel="stylesheet" href="https://fonts.googleapis.com/css2?family=Roboto:ital,wght@0,400;0,500;0,700;1,700&family=Roboto+Condensed:wght@400;700&display=swap">
<style>
  :root {
    --stage: #e9e9ea;
    --silver-light: #ffffff;
    --silver-mid: #e6e7e9;
    --silver-dark: #c9cbce;
    --swoosh: rgba(255,255,255,0.55);
    --swoosh-shade: rgba(160,163,168,0.18);
    --brand-blue: #1565b8;
    --brand-green: #2f8f3a;
    --ink: #1f2226;
    --card-shadow: 0 14px 30px rgba(0,0,0,0.28);
  }
  * { box-sizing: border-box; margin: 0; padding: 0; }
  html, body { width: 1200px; height: 1000px; overflow: hidden; }
  body { background: var(--stage); position: relative; font-family: "Roboto", sans-serif; }

  .card {
    position: absolute;
    width: 600px;
    height: 343px;
    border-radius: 4px;
    overflow: hidden;
    background: linear-gradient(135deg, var(--silver-dark) 0%, var(--silver-light) 45%, var(--silver-mid) 75%, var(--silver-dark) 100%);
    box-shadow: var(--card-shadow);
  }
  .card-front { left: 90px; top: 120px; }
  .card-back { left: 510px; top: 540px; }

  .card-swoosh { position: absolute; inset: 0; width: 100%; height: 100%; }

  /* Front: firm identity */
  .firm-id {
    position: absolute;
    left: 148px; top: 48px;
    display: flex; align-items: center; gap: 12px;
  }
  .firm-mark {
    font-family: "Roboto", sans-serif;
    font-weight: 700;
    font-size: 46px;
    color: var(--brand-blue);
    letter-spacing: 1px;
    line-height: 1;
  }
  .firm-divider { width: 2px; height: 54px; background: var(--brand-blue); }
  .firm-name {
    font-family: "Roboto", sans-serif;
    font-weight: 700;
    font-size: 18px;
    line-height: 18px;
    color: var(--brand-blue);
    text-transform: uppercase;
    letter-spacing: 0.5px;
  }

  /* Front: person */
  .person { position: absolute; left: 36px; top: 196px; width: 250px; }
  .person-name {
    font-family: "Roboto Condensed", sans-serif;
    font-weight: 700;
    font-size: 19px;
    color: var(--brand-blue);
    padding-left: 6px;
    padding-bottom: 3px;
    border-bottom: 1.5px solid var(--brand-green);
  }
  .person-title {
    font-family: "Roboto", sans-serif;
    font-style: italic;
    font-weight: 700;
    font-size: 11.5px;
    color: var(--brand-green);
    margin-top: 5px;
    padding-left: 18px;
  }

  /* Front: contact list */
  .contact-list { position: absolute; left: 352px; top: 203px; list-style: none; }
  .contact-item {
    display: flex; align-items: center; gap: 9px;
    font-family: "Roboto Condensed", sans-serif;
    font-size: 17px;
    color: var(--ink);
    height: 28px;
  }
  .contact-icon {
    width: 17px; height: 17px;
    border-radius: 3px;
    background: var(--brand-blue);
    display: flex; align-items: center; justify-content: center;
    flex: none;
  }

  /* Back: large identity */
  .back-id {
    position: absolute;
    left: 0; right: 0; top: 0; bottom: 0;
    display: flex; align-items: center; justify-content: center; gap: 18px;
  }
  .back-square { width: 46px; height: 46px; background: var(--brand-green); }
  .back-mark {
    font-family: "Roboto", sans-serif;
    font-weight: 700;
    font-size: 110px;
    color: var(--brand-blue);
    letter-spacing: 2px;
    line-height: 1;
  }
</style>
</head>
<body>

  <section class="card card-front" aria-label="Business card front">
    <svg class="card-swoosh" viewBox="0 0 600 343" preserveAspectRatio="none" aria-hidden="true">
      <path d="M0 0 H230 C120 60 70 140 150 230 C200 290 190 320 170 343 H0 Z" fill="var(--swoosh)"/>
      <path d="M230 0 C120 60 70 140 150 230 C200 290 190 320 170 343" fill="none" stroke="var(--swoosh-shade)" stroke-width="3"/>
      <path d="M600 10 C470 30 330 40 260 30" fill="none" stroke="var(--swoosh-shade)" stroke-width="2"/>
    </svg>

    <div class="firm-id">
      <span class="firm-mark">KTW</span>
      <span class="firm-divider"></span>
      <span class="firm-name">Northbank<br>Professional<br>Corporation</span>
    </div>

    <div class="person">
      <p class="person-name">Daniel Moreau CPA, CGA.</p>
      <p class="person-title">PRINCIPAL AND SENIOR CONSULTANT</p>
    </div>

    <ul class="contact-list">
      <li class="contact-item">
        <span class="contact-icon">
          <svg width="11" height="11" viewBox="0 0 24 24" aria-hidden="true"><path fill="#fff" d="M6.6 10.8a15 15 0 0 0 6.6 6.6l2.2-2.2c.3-.3.7-.4 1-.2 1.1.4 2.3.6 3.6.6.6 0 1 .4 1 1V20c0 .6-.4 1-1 1A17 17 0 0 1 3 4c0-.6.4-1 1-1h3.5c.6 0 1 .4 1 1 0 1.3.2 2.5.6 3.6.1.3 0 .7-.2 1z"/></svg>
        </span>(780) 555-0142
      </li>
      <li class="contact-item">
        <span class="contact-icon">
          <svg width="11" height="11" viewBox="0 0 24 24" aria-hidden="true"><rect x="6" y="2" width="12" height="20" rx="2" fill="#fff"/><rect x="8" y="5" width="8" height="12" fill="var(--brand-blue)"/></svg>
        </span>(780) 555-0187
      </li>
      <li class="contact-item">
        <span class="contact-icon">
          <svg width="11" height="11" viewBox="0 0 24 24" aria-hidden="true"><rect x="2" y="5" width="20" height="14" rx="1" fill="#fff"/><path d="M2 6l10 7 10-7" fill="none" stroke="var(--brand-blue)" stroke-width="2"/></svg>
        </span>daniel@ktw-cpa.com
      </li>
      <li class="contact-item">
        <span class="contact-icon">
          <svg width="11" height="11" viewBox="0 0 24 24" aria-hidden="true"><circle cx="12" cy="12" r="9" fill="none" stroke="#fff" stroke-width="2"/><ellipse cx="12" cy="12" rx="4" ry="9" fill="none" stroke="#fff" stroke-width="1.6"/><path d="M3 12h18" stroke="#fff" stroke-width="1.6"/></svg>
        </span>www.ktw-cpa.com
      </li>
    </ul>
  </section>

  <section class="card card-back" aria-label="Business card reverse">
    <svg class="card-swoosh" viewBox="0 0 600 343" preserveAspectRatio="none" aria-hidden="true">
      <path d="M0 0 H200 C100 70 60 160 140 240 C180 285 170 320 150 343 H0 Z" fill="var(--swoosh)"/>
      <path d="M200 0 C100 70 60 160 140 240 C180 285 170 320 150 343" fill="none" stroke="var(--swoosh-shade)" stroke-width="3"/>
    </svg>
    <div class="back-id">
      <span class="back-square"></span>
      <span class="back-mark">KTW</span>
    </div>
  </section>

</body>
</html>
```